Postcard Design Project A Healthy reminder

Dr.'s Jeetesh and Lorna sethi. Internal Medicine/Family practice. This postcard will be for our patients that we have not seen in a while. Also we need another postcard (the one your designing) with a different heading for New patient's. Do you offer a price break for that? The only thing we would need to change is the heading. Please let me know. Thank you so much! Also can you use the map on the last postcard and our logo I made? I cant find it. Please feel free to call me or email me.

```html
<!DOCTYPE html>
<html lang="en">
<head>
<meta charset="utf-8">
<title>A Healthy Reminder – Postcard</title>
<link rel="stylesheet" href="https://fonts.googleapis.com/css2?family=Fira+Sans:wght@700;800&family=Lato:wght@400;700&display=swap">
<style>
  :root {
    --backdrop: #a9a9a9;
    --paper: #f7f6f3;
    --paper-back: #f3f0e9;
    --maroon: #7a1419;
    --ink: #222222;
    --grey-band: #8d8d8d;
    --grey-text: #5d5d5d;
    --rule: #9a9a9a;
  }
  * { box-sizing: border-box; margin: 0; padding: 0; }
  html, body { width: 1200px; height: 962px; overflow: hidden; }
  body {
    background: var(--backdrop);
    font-family: "Lato", Arial, sans-serif;
    position: relative;
  }
  .card {
    position: absolute;
    width: 660px;
    height: 440px;
    overflow: hidden;
  }
  .card--front { left: 500px; top: 30px; background: var(--paper); }
  .card--back { left: 40px; top: 495px; background: var(--paper-back); }

  .card-art { position: absolute; inset: 0; }

  /* Brand lockup */
  .brand { position: absolute; display: flex; flex-direction: column; }
  .brand-name {
    display: flex; align-items: center; gap: 8px;
    font-family: "Lato", Arial, sans-serif;
    font-weight: 700; font-size: 16px; color: var(--grey-text);
  }
  .brand-mark { width: 12px; height: 12px; background: var(--maroon); }
  .brand-tagline {
    margin-top: 6px; margin-left: 20px;
    font-size: 8px; font-weight: 700; letter-spacing: 1.4px;
    color: var(--grey-text);
  }
  .card--front .brand { left: 48px; top: 40px; }
  .card--back .brand { left: 40px; top: 36px; }
  .card--back .brand-name { color: var(--ink); font-size: 18px; }
  .card--back .brand-tagline { font-size: 9px; color: var(--ink); }

  .stethoscope-art {
    position: absolute; left: 260px; top: 24px;
    width: 120px; height: 72px; border-radius: 10px;
    background: radial-gradient(ellipse at center, #d6d6d6, #eeeeec 70%);
  }

  .headline {
    position: absolute; left: 38px; top: 110px;
    font-family: "Fira Sans", Arial, sans-serif;
    color: var(--maroon); line-height: 1;
  }
  .headline-main { display: block; font-weight: 800; font-size: 35px; letter-spacing: -0.3px; }
  .headline-sub { display: block; margin-top: 6px; font-weight: 700; font-size: 19px; }

  .features { position: absolute; left: 30px; top: 180px; width: 370px; list-style: none; }
  .feature { display: flex; gap: 14px; padding: 3px 0; }
  .feature-icon { flex: 0 0 30px; height: 30px; margin-top: 4px; }
  .feature-title {
    font-family: "Fira Sans", Arial, sans-serif; font-weight: 700;
    font-size: 13px; line-height: 16px; color: var(--maroon);
  }
  .feature-text { font-size: 12px; line-height: 15px; color: var(--ink); }
  .feature-rule { height: 2px; width: 220px; margin: 3px 0 3px 44px; background: var(--rule); }

  .web-band {
    position: absolute; left: 0; top: 352px;
    width: 420px; height: 38px;
    background: var(--grey-band);
    display: flex; align-items: center; padding-left: 30px;
    font-weight: 700; font-size: 18px; color: #ffffff; letter-spacing: 0.3px;
  }

  /* Back */
  .map-art {
    position: absolute; left: 40px; top: 112px;
    width: 300px; height: 92px; border-radius: 18px;
    border: 3px solid var(--maroon);
    background: linear-gradient(135deg, #e7e3da, #d9d6cd 60%, #e4e0d6);
  }
  .contact { position: absolute; left: 40px; top: 216px; color: var(--maroon); }
  .contact-address { font-size: 10px; font-weight: 700; }
  .contact-phone {
    font-family: "Fira Sans", Arial, sans-serif; font-weight: 800;
    font-size: 25px; line-height: 1.1; margin-top: 2px;
  }
  .contact-web { font-size: 11px; font-weight: 700; letter-spacing: 4px; }

  .stamp-box {
    position: absolute; right: 44px; top: 36px;
    width: 110px; height: 60px; border: 1.5px solid #333;
  }
  .address-line { position: absolute; left: 430px; width: 190px; height: 1px; background: #555; }
</style>
</head>
<body>

<section class="card card--front" aria-label="Postcard front">
  <div class="brand">
    <div class="brand-name"><span class="brand-mark"></span>Jeetesh T Sethi, M.D.</div>
    <div class="brand-tagline">A Primary Care Office</div>
  </div>

  <div class="stethoscope-art" role="img" aria-label="Stethoscope illustration"></div>

  <h1 class="headline">
    <span class="headline-main">A HEALTHY REMINDER.</span>
    <span class="headline-sub">IT IS TIME FOR YOUR ANNUAL EXAMS</span>
  </h1>

  <ul class="features">
    <li class="feature">
      <svg class="feature-icon" viewBox="0 0 32 32" fill="none" stroke="#8a8a8a" stroke-width="1.6" aria-hidden="true">
        <ellipse cx="16" cy="16" rx="14" ry="5.5"/>
        <ellipse cx="16" cy="16" rx="14" ry="5.5" transform="rotate(60 16 16)"/>
        <ellipse cx="16" cy="16" rx="14" ry="5.5" transform="rotate(120 16 16)"/>
        <circle cx="16" cy="16" r="2" fill="#8a8a8a"/>
      </svg>
      <div>
        <div class="feature-title">Experienced</div>
        <p class="feature-text">Over 20 years of experience practicing in primary<br>care and internal medicine.</p>
      </div>
    </li>
    <li class="feature-rule" aria-hidden="true"></li>
    <li class="feature">
      <svg class="feature-icon" viewBox="0 0 32 32" fill="none" stroke="#8a8a8a" stroke-width="1.8" aria-hidden="true">
        <circle cx="16" cy="16" r="14"/>
        <path d="M9.5 16.5 L14 21 L22.5 11.5"/>
      </svg>
      <div>
        <div class="feature-title">Professional</div>
        <p class="feature-text">We maintain exceptional standards of patient care.</p>
      </div>
    </li>
    <li class="feature-rule" aria-hidden="true"></li>
    <li class="feature">
      <svg class="feature-icon" viewBox="0 0 32 32" fill="none" stroke="#8a8a8a" stroke-width="1.8" aria-hidden="true">
        <path d="M16 28 C6 20 2 15 2 10 A7 7 0 0 1 16 8 A7 7 0 0 1 30 10 C30 15 26 20 16 28 Z"/>
      </svg>
      <div>
        <div class="feature-title">Compassionate</div>
        <p class="feature-text">Commited to providing quality healthcare to<br>our patients we are privileged to serve.</p>
      </div>
    </li>
  </ul>

  <div class="web-band">www.sethifamilymd.com</div>

  <svg class="card-art" viewBox="0 0 660 440">
    <defs>
      <linearGradient id="photoTone" x1="0" y1="0" x2="1" y2="1">
        <stop offset="0" stop-color="#d9cdbd"/>
        <stop offset="0.5" stop-color="#c9c2b6"/>
        <stop offset="1" stop-color="#a9aaa6"/>
      </linearGradient>
    </defs>
    <path role="img" aria-label="Photo of two doctors in white coats reviewing charts in a clinic hallway"
          d="M408 0 C452 120 448 300 336 440 L660 440 L660 0 Z" fill="url(#photoTone)"/>
    <path d="M384 0 C428 120 424 300 312 440" fill="none" stroke="var(--maroon)" stroke-width="3"/>
    <path d="M396 0 C440 120 436 300 324 440" fill="none" stroke="var(--maroon)" stroke-width="3"/>
  </svg>
</section>

<section class="card card--back" aria-label="Postcard back">
  <svg class="card-art" viewBox="0 0 660 440" aria-hidden="true">
    <path d="M440 0 C370 110 340 300 370 440" fill="none" stroke="var(--maroon)" stroke-width="3"/>
    <path d="M452 0 C382 110 352 300 382 440" fill="none" stroke="var(--maroon)" stroke-width="3"/>
  </svg>

  <div class="brand">
    <div class="brand-name"><span class="brand-mark"></span>Jeetesh T Sethi, M.D.</div>
    <div class="brand-tagline">A Primary Care Office</div>
  </div>

  <div class="map-art" role="img" aria-label="Map showing the office location"></div>

  <div class="contact">
    <p class="contact-address">4815 N. Alder Avenue Suite 210, Fresno, Ca 93711</p>
    <p class="contact-phone">Office (555) 014-2267</p>
    <p class="contact-web">www.sethifamilymd.com</p>
  </div>

  <div class="stamp-box" aria-label="Stamp area"></div>
  <div class="address-line" style="top:270px"></div>
  <div class="address-line" style="top:305px"></div>
  <div class="address-line" style="top:340px"></div>
</section>

</body>
</html>
```